Health Coaching Flyer for New Clients

I need a two-sided flyer (3.5" x 8.5" preferred or 5" x 7") to distribute to potential coaching clients. My business name is Talvora Health & Wellness Coaching. My business is focused on helping people with habit changes that contribute to their overall well-being. I would like the design colors to be gender neutral. I would like a small photo of myself near the "my name is Jen" statement. Please feel free to change the logo color to match the design.

Target Market(s)

Adults of all ages.

Font styles to use
Serif

Requirements
Must have
• Emphasize my opening question (found in health coaching brochure - attached).
• Small picture of myself near "my name is Jen" statement.
Should not have
• No light of pastel colors.

```html
<!DOCTYPE html>
<html lang="en">
<head>
<meta charset="utf-8">
<title>Talvora Health &amp; Wellness Coaching – Flyer</title>
<link rel="stylesheet" href="https://fonts.googleapis.com/css2?family=Cabin:wght@400;500;600;700&family=Roboto+Condensed:wght@700&display=swap">
<style>
  :root{
    --backdrop:#737373;
    --navy:#255a72;
    --navy-deep:#1f4d63;
    --sky:#5b93d3;
    --sky-line:#4f86cf;
    --ink:#333a40;
    --white:#ffffff;
    --yellow:#f4e82a;
  }
  *{box-sizing:border-box;margin:0;padding:0}
  html,body{width:1200px;height:1200px;overflow:hidden;background:var(--backdrop)}
  body{position:relative;font-family:"Cabin",sans-serif;color:var(--ink)}
  .panel{position:absolute;top:64px;width:438px;height:1062px;background:var(--white);overflow:hidden}
  .panel--front{left:165px}
  .panel--back{left:629px}
  .abs{position:absolute}

  /* brand */
  .brand{position:absolute;left:0;right:0;text-align:center;font-weight:700;line-height:1}
  .brand__name{display:block;font-size:44px;letter-spacing:3px}
  .brand__tag{display:block;font-size:12px;letter-spacing:.5px;margin-top:6px;text-transform:uppercase}
  .panel--front .brand{top:34px;color:#111}
  .panel--back .brand{top:30px;color:var(--white)}

  /* front */
  .frame{position:absolute;left:21px;top:56px;width:394px;height:502px;border:1.5px solid var(--sky-line);border-bottom:none}
  .frame-gap{position:absolute;top:50px;left:45px;width:348px;height:12px;background:var(--white)}
  .hero-photo{position:absolute;left:0;top:92px;width:437px;height:466px;
    background:radial-gradient(ellipse at 55% 55%,#b8c0c4 0%,#dfe4e8 45%,#f3f6f9 100%)}
  .frame-side{position:absolute;top:56px;height:502px;border-left:1.5px solid var(--sky-line)}
  .sheen{position:absolute;left:0;width:100%;height:13px;background:linear-gradient(#d8dde0,#8fa3ad)}
  .band-dark{position:absolute;left:0;width:100%;background:var(--navy)}
  .headline{font-family:"Roboto Condensed",sans-serif;font-weight:700;text-transform:uppercase;position:absolute;left:22px;line-height:1}
  .headline--lead{top:581px;font-size:48px;color:var(--white)}
  .headline--mid{top:632px;font-size:24px;color:var(--white)}
  .headline--end{top:687px;font-size:39px;color:var(--navy)}
  .intro{position:absolute;left:22px;top:799px;width:393px;font-size:13.6px;line-height:16.8px;text-align:justify;text-align-last:center;font-weight:500}

  /* contact footer */
  .contact-band{position:absolute;left:0;top:942px;width:100%;height:120px;background:linear-gradient(#5b93d3,#2f6188)}
  .portrait{position:absolute;left:23px;top:917px;width:94px;height:124px;background:var(--white);padding:0}
  .portrait__photo{position:absolute;left:0;top:0;width:94px;height:104px;background:linear-gradient(160deg,#6b4a3a,#b27a62 55%,#3b2a22)}
  .portrait__name{position:absolute;left:0;bottom:4px;width:100%;text-align:center;font-size:9px;font-weight:700;color:var(--navy)}
  .contact-pill{position:absolute;left:121px;top:918px;width:294px;height:53px;background:var(--white);border:1.5px solid var(--sky-line);border-radius:26px;text-align:center;padding-top:5px}
  .contact-pill__title{font-size:16px;font-weight:700;color:var(--navy);line-height:1}
  .contact-pill__sub{font-size:11px;line-height:12.5px;margin-top:2px}
  .phone{position:absolute;left:161px;top:984px;font-size:38px;font-weight:600;color:var(--white);line-height:1}
  .email{position:absolute;left:161px;top:1026px;font-size:15.5px;font-weight:500;color:var(--white)}
  .icon{position:absolute;left:132px}

  /* back */
  .header-band{position:absolute;left:0;top:0;width:100%;height:114px;background:var(--navy)}
  .section-title{position:absolute;left:22px;top:143px;font-size:29px;font-weight:600;color:var(--navy)}
  .section-rule{position:absolute;left:22px;top:178px;width:33px;height:3px;background:var(--sky-line)}
  .benefits{position:absolute;left:26px;top:196px;width:400px;list-style:none;font-size:15px;line-height:18.8px;font-weight:600}
  .benefits li{position:relative;padding-left:15px}
  .benefits li::before{content:"";position:absolute;left:0;top:6px;width:8px;height:8px;border-radius:50%;background:var(--sky-line)}
  .invite-band{position:absolute;left:0;top:462px;width:100%;height:132px;background:var(--sky)}
  .invite-pill{position:absolute;left:23px;top:434px;width:394px;height:97px;background:var(--white);border:1.5px solid var(--navy);border-radius:48px;text-align:center;padding-top:20px;color:var(--navy)}
  .invite-pill__lead{font-size:20px;font-weight:600;line-height:1}
  .invite-pill__rest{font-size:15.5px;font-weight:500;line-height:19px;margin-top:3px}
  .plan-note{position:absolute;left:0;top:542px;width:100%;text-align:center;font-size:15.5px;font-weight:600;line-height:20px;color:var(--white)}
  .giveback{position:absolute;left:0;width:100%;text-align:center;color:var(--navy);font-weight:600;line-height:1}
  .giveback--lead{top:613px;font-size:35px}
  .giveback--sub{top:651px;font-size:19px}
  .giveback--sub em{font-style:normal;color:var(--sky-line)}
  .offer-pill{position:absolute;left:22px;top:686px;width:393px;height:70px;border-radius:35px;background:var(--navy);color:var(--yellow);text-align:center;font-size:24px;font-weight:700;line-height:70px;letter-spacing:-.3px}
  .limited{position:absolute;left:0;top:764px;width:100%;text-align:center;font-size:19px;font-weight:500;color:#222}
  .stones-photo{position:absolute;left:83px;top:792px;width:272px;height:120px;border-radius:50%;
    background:radial-gradient(ellipse at 50% 60%,#c9c9c9 0%,#e6e6e6 40%,rgba(255,255,255,0) 72%)}
</style>
</head>
<body>

<!-- Front side -->
<section class="panel panel--front">
  <div class="hero-photo" role="img" aria-label="Photo of a woman in workout clothes stretching on the floor, reaching toward her sneakers in a bright studio"></div>
  <div class="frame-side" style="left:21px"></div>
  <div class="frame-side" style="left:415px"></div>
  <div class="abs" style="left:21px;top:56px;width:24px;border-top:1.5px solid var(--sky-line)"></div>
  <div class="abs" style="left:391px;top:56px;width:25px;border-top:1.5px solid var(--sky-line)"></div>
  <div class="abs" style="left:40px;top:30px;width:356px;height:70px;background:var(--white)"></div>
  <div class="brand">
    <span class="brand__name">TALVORA</span>
    <span class="brand__tag">Health &amp; Wellness Coaching</span>
  </div>

  <div class="sheen" style="top:558px"></div>
  <div class="band-dark" style="top:570px;height:107px"></div>
  <div class="headline headline--lead">Need support in</div>
  <div class="headline headline--mid">Making real, lasting lifestyle and</div>
  <div class="headline headline--end">Behavior changes?</div>
  <div class="band-dark" style="top:734px;height:28px"></div>
  <div class="sheen" style="top:762px;background:linear-gradient(#8fa3ad,#eef1f3)"></div>

  <p class="intro">I am studying to become an ARISE-Certified Functional Health Coach. My training involves many science-based practices that improve both our health and how we grow and change as humans. I now have the opportunity to turn that knowledge into practice by coaching actual clients interested in improving their own health and well-being.</p>

  <div class="contact-band"></div>
  <div class="portrait">
    <div class="portrait__photo" role="img" aria-label="Small portrait photo of Jen Talvora"></div>
    <div class="portrait__name">JEN TALVORA</div>
  </div>
  <div class="contact-pill">
    <div class="contact-pill__title">Please contact me</div>
    <div class="contact-pill__sub">I'm ready to support you as you work to<br>improve your health.</div>
  </div>
  <svg class="icon" style="top:1004px" width="16" height="16" viewBox="0 0 24 24" aria-hidden="true"><path fill="#fff" d="M6.6 10.8a15.1 15.1 0 0 0 6.6 6.6l2.2-2.2a1 1 0 0 1 1-.25 11.4 11.4 0 0 0 3.6.57 1 1 0 0 1 1 1V20a1 1 0 0 1-1 1A17 17 0 0 1 3 4a1 1 0 0 1 1-1h3.5a1 1 0 0 1 1 1c0 1.25.2 2.45.57 3.57a1 1 0 0 1-.25 1z"/></svg>
  <div class="phone">520-555-0148</div>
  <svg class="icon" style="top:1029px" width="14" height="14" viewBox="0 0 24 24" aria-hidden="true"><g fill="none" stroke="#fff" stroke-width="2"><circle cx="12" cy="12" r="10"/><ellipse cx="12" cy="12" rx="4.5" ry="10"/><path d="M2 12h20M4 7h16M4 17h16"/></g></svg>
  <div class="email">talvorahwc@example.com</div>
</section>

<!-- Back side -->
<section class="panel panel--back">
  <div class="header-band"></div>
  <div class="brand">
    <span class="brand__name">TALVORA</span>
    <span class="brand__tag">Health &amp; Wellness Coaching</span>
  </div>

  <h2 class="section-title">Functional health coaches</h2>
  <div class="section-rule"></div>
  <ul class="benefits">
    <li>Leverage your strengths rather than focus on<br>your weaknesses</li>
    <li>Support you in finding your own strategies and motivation for change</li>
    <li>Provide a judgment-free zone and support<br>your autonomy</li>
    <li>Use an experimental mindset to find and develop sustainable habits</li>
    <li>Act as your accountability partner as you reach your unique health goals; whether they be improving sleep, diet, fitness, social connection, or reducing stress.</li>
  </ul>

  <div class="invite-band"></div>
  <div class="invite-pill">
    <div class="invite-pill__lead">I would like to invite you to participate</div>
    <div class="invite-pill__rest">with me as a client as I continue to<br>hone my coaching skills</div>
  </div>
  <p class="plan-note">We can develop a plan and schedule that aligns<br>with your goals.</p>

  <div class="giveback giveback--lead">As a way to give back to</div>
  <div class="giveback giveback--sub">my community, <em>I am offering new clients</em></div>
  <div class="offer-pill">SIX FREE COACHING SESSIONS</div>
  <div class="limited">This is a limited time offer.</div>
  <div class="stones-photo" role="img" aria-label="Photo of stacked grey spa stones with a purple orchid and green leaves"></div>

  <div class="contact-band"></div>
  <div class="portrait">
    <div class="portrait__photo" role="img" aria-label="Small portrait photo of Jen Talvora"></div>
    <div class="portrait__name">JEN TALVORA</div>
  </div>
  <div class="contact-pill">
    <div class="contact-pill__title">Please contact me</div>
    <div class="contact-pill__sub">I'm ready to support you as you work to<br>improve your health.</div>
  </div>
  <svg class="icon" style="top:1004px" width="16" height="16" viewBox="0 0 24 24" aria-hidden="true"><path fill="#fff" d="M6.6 10.8a15.1 15.1 0 0 0 6.6 6.6l2.2-2.2a1 1 0 0 1 1-.25 11.4 11.4 0 0 0 3.6.57 1 1 0 0 1 1 1V20a1 1 0 0 1-1 1A17 17 0 0 1 3 4a1 1 0 0 1 1-1h3.5a1 1 0 0 1 1 1c0 1.25.2 2.45.57 3.57a1 1 0 0 1-.25 1z"/></svg>
  <div class="phone">520-555-0148</div>
  <svg class="icon" style="top:1029px" width="14" height="14" viewBox="0 0 24 24" aria-hidden="true"><g fill="none" stroke="#fff" stroke-width="2"><circle cx="12" cy="12" r="10"/><ellipse cx="12" cy="12" rx="4.5" ry="10"/><path d="M2 12h20M4 7h16M4 17h16"/></g></svg>
  <div class="email">talvorahwc@example.com</div>
</section>

</body>
</html>
```